KTR Engineering Pty Ltd

I have already had Corvale welding and fabrication cards made , my business has changed too KTR engineering Pty Ltd so I need my logo changed on the cards
one side have my logo then the other side have what we do.
front side logo and details
owner /operator : Lachlan Meravic
email: ktr.works@ironvalemail.com
number: 0491537204
ABN: 47 261 538 902
ACN: 718 352 946
on back have in dot points what we do:
* structural steel erection
* precast panels
* site welding
*steel alteration & repair
* rigging & dogging
*labour hire
all details in breif

```html
<!DOCTYPE html>
<html lang="en">
<head>
<meta charset="utf-8">
<title>KTR Engineering Pty Ltd – Business Card</title>
<link rel="stylesheet" href="https://fonts.googleapis.com/css2?family=Poppins:wght@400;500;600;700&display=swap">
<style>
  :root {
    --backdrop: #7f9aba;
    --paper: #ffffff;
    --navy: #25303d;
    --rust: #9b4a3e;
    --ink: #1f1f1f;
    --band-text: #ffffff;
  }
  * { box-sizing: border-box; margin: 0; padding: 0; }
  html, body {
    width: 1200px; height: 876px; overflow: hidden;
    background: var(--backdrop);
    font-family: "Poppins", sans-serif;
  }
  .sheet {
    width: 1200px; height: 876px;
    display: flex; align-items: center; justify-content: center; gap: 44px;
  }
  .card {
    position: relative;
    width: 530px; height: 322px;
    background: var(--paper);
    box-shadow: 0 14px 30px rgba(30, 45, 70, 0.35);
    overflow: hidden;
  }

  /* Brand wordmark */
  .brand { display: flex; flex-direction: column; align-items: flex-start; }
  .brand-row { display: flex; align-items: center; gap: 10px; }
  .brand-mark { width: 14px; height: 14px; background: var(--rust); flex: none; }
  .brand-name {
    font-weight: 700; color: var(--navy);
    font-size: 21px; line-height: 1.15; letter-spacing: 0.3px;
  }
  .brand-phone {
    margin-top: 4px; margin-left: 24px;
    font-weight: 600; font-size: 12px; color: var(--rust); letter-spacing: 0.5px;
  }

  /* Front */
  .card-front .brand { position: absolute; left: 34px; top: 70px; width: 250px; }
  .card-front .brand-name { font-size: 19px; }
  .divider {
    position: absolute; left: 300px; top: 92px;
    width: 2px; height: 170px; background: var(--rust);
  }
  .contact { position: absolute; left: 318px; top: 96px; color: var(--ink); }
  .contact-name { font-weight: 600; font-size: 20px; letter-spacing: 1.4px; line-height: 1.1; }
  .contact-role { font-size: 12px; letter-spacing: 1px; margin: 2px 0 10px; color: #333; }
  .contact-line { display: flex; align-items: center; gap: 6px; font-size: 11.5px; margin-bottom: 5px; }
  .contact-icon {
    width: 15px; height: 15px; border-radius: 3px; background: var(--rust);
    display: flex; align-items: center; justify-content: center; flex: none;
  }
  .reg { font-size: 11.5px; margin-top: 6px; line-height: 1.5; }
  .reg-label { font-weight: 600; color: var(--rust); }

  /* Back */
  .card-back .brand { position: absolute; left: 150px; top: 40px; }
  .card-back .brand-name { font-size: 24px; }
  .service-band {
    position: absolute; left: 0; top: 136px; width: 100%; height: 74px;
    background: var(--rust);
    display: grid; grid-template-columns: 1.25fr 1fr 0.9fr;
    align-content: center; row-gap: 8px; padding: 0 18px;
    list-style: none;
  }
  .service {
    color: var(--band-text); font-size: 11.5px; letter-spacing: 0.6px; white-space: nowrap;
  }
  .service::before {
    content: ""; display: inline-block; width: 5px; height: 5px; border-radius: 50%;
    background: var(--band-text); margin-right: 6px; vertical-align: middle;
  }
</style>
</head>
<body>
<main class="sheet">

  <section class="card card-front" aria-label="Business card front">
    <div class="brand">
      <div class="brand-row">
        <span class="brand-mark"></span>
        <span class="brand-name">KTR Engineering Pty Ltd</span>
      </div>
      <span class="brand-phone">0491537204</span>
    </div>
    <span class="divider"></span>
    <div class="contact">
      <p class="contact-name">Lachlan Meravic</p>
      <p class="contact-role">Owner/Operator</p>
      <p class="contact-line">
        <span class="contact-icon">
          <svg width="9" height="9" viewBox="0 0 24 24" aria-hidden="true"><path fill="#fff" d="M6.6 10.8a15.1 15.1 0 0 0 6.6 6.6l2.2-2.2a1 1 0 0 1 1-.25 11.4 11.4 0 0 0 3.6.57 1 1 0 0 1 1 1V20a1 1 0 0 1-1 1A17 17 0 0 1 3 4a1 1 0 0 1 1-1h3.5a1 1 0 0 1 1 1c0 1.25.2 2.45.57 3.6a1 1 0 0 1-.25 1z"/></svg>
        </span>
        0491537204
      </p>
      <p class="contact-line">
        <span class="contact-icon">
          <svg width="10" height="8" viewBox="0 0 24 18" aria-hidden="true"><rect x="1" y="1" width="22" height="16" rx="2" fill="none" stroke="#fff" stroke-width="2.5"/><path d="M2 2l10 8 10-8" fill="none" stroke="#fff" stroke-width="2.5"/></svg>
        </span>
        ktr.works@ironvalemail.com
      </p>
      <p class="reg"><span class="reg-label">ABN:</span> 47 261 538 902<br><span class="reg-label">ACN:</span> 718 352 946</p>
    </div>
  </section>

  <section class="card card-back" aria-label="Business card back">
    <div class="brand">
      <div class="brand-row">
        <span class="brand-mark"></span>
        <span class="brand-name">KTR Engineering Pty Ltd</span>
      </div>
      <span class="brand-phone">0491537204</span>
    </div>
    <ul class="service-band">
      <li class="service">Structural steel erection</li>
      <li class="service">Precast panels</li>
      <li class="service">Site welding</li>
      <li class="service">Steel alteration &amp; repair</li>
      <li class="service">Rigging &amp; dogging</li>
      <li class="service">Labour hire</li>
    </ul>
  </section>

</main>
</body>
</html>
```